Bright Kestrel Studio - Redesign of our website - needs to be dynamic and alive!

We provide fun lessons exclusively in students' homes in music, art, yoga and acting. I like most of the graphics and copy on the site now, but it looks too static and there might be too much info to read on the home page. Needs movement, needs to generate excitement and be a fun place to visit, yet keeping professional-looking. The site needs better SEO, a better look and needs to generate more business, as several people see it each day but few contact us for details about our program. The site is brightkestrel-studio.test. I'd like it to continue to be hosted on my domain in Wordpress format so I can add and delete teacher photos from time to time. I like the way the teachers' bios currently pop up when a cursor is hovered over them on the Our Team page. Thank you and good luck!

Target Market(s)

Wealthy, college-educated households with children who live in the Greater Atlanta area

Industry/Entity Type

Education

Coding

Number of Pages Required

Requirements
Must have
• Home Page movement, excitement, but keeping it professional-looking. We're an educational company and want to market to people who are looking for a professional yet fun/exciting approach to lessons in their homes.
Nice to have
• The info on the Testimonials page can probably rotate and fade in/fade out on the home page or slide on/slide off instead of having a separate page for these.
• The info on the Trial Lessons page can probably be included as a banner on the home page too instead of being a separate page. Nice if I can change the text on this myself from time to time to mention any promotions I might be offering with regard to trial lessons.

```html
<!DOCTYPE html>
<html lang="en">
<head>
<meta charset="utf-8">
<title>Bright Kestrel Studio – In-Home Lessons in Atlanta</title>
<link rel="stylesheet" href="https://fonts.googleapis.com/css2?family=Marcellus&family=Marcellus+SC&family=Open+Sans:wght@400;600;700&display=swap">
<style>
  :root {
    --purple: #4b2182;
    --purple-dark: #3d1a6c;
    --cyan: #1ea9d6;
    --cyan-light: #35c1e6;
    --orange: #ef7a27;
    --amber: #f7a11a;
    --green: #72b84b;
    --grey-bg: #ececec;
    --field: #ededed;
    --text: #555;
    --white: #fff;
  }
  * { box-sizing: border-box; margin: 0; padding: 0; }
  html, body { width: 1200px; height: 3550px; overflow: hidden; }
  body { font-family: "Open Sans", sans-serif; color: var(--text); background: var(--white); }
  .section-title { font-family: "Marcellus", serif; font-weight: 400; text-align: center; font-size: 44px; letter-spacing: 1px; }

  /* header */
  .site-header { height: 125px; display: flex; align-items: center; justify-content: space-between; padding: 0 78px; }
  .brand { display: flex; align-items: center; gap: 12px; }
  .brand-mark { width: 44px; height: 44px; border-radius: 50%; background: var(--cyan); }
  .brand-name { font-family: "Open Sans", sans-serif; font-weight: 700; font-size: 26px; color: var(--purple); line-height: 1.05; width: 170px; }
  .call { display: flex; align-items: center; gap: 14px; }
  .call-label { color: var(--cyan); font-size: 18px; }
  .call-number { color: var(--cyan); font-weight: 700; font-size: 28px; }

  /* nav */
  .main-nav { height: 57px; background: var(--purple); padding-left: 78px; display: flex; }
  .main-nav a { font-family: "Marcellus", serif; color: var(--white); text-decoration: none; font-size: 19px; padding: 0 19px; display: flex; align-items: center; }
  .main-nav a.active { background: var(--cyan); }

  /* hero */
  .hero { height: 575px; position: relative; background: linear-gradient(120deg, #3a3430 0%, #6b625a 35%, #4a403a 60%, #8a8078 80%, #3e3632 100%); text-align: center; color: var(--white); }
  .hero::after { content: ""; position: absolute; inset: 0; background: rgba(0,0,0,.35); }
  .hero-inner { position: relative; z-index: 1; padding-top: 178px; }
  .hero h1 { font-family: "Open Sans", sans-serif; font-weight: 700; font-size: 50px; letter-spacing: 1px; }
  .hero p { font-size: 22px; margin-top: 18px; }
  .btn { display: inline-flex; align-items: center; gap: 8px; border-radius: 30px; color: var(--white); text-decoration: none; font-weight: 600; }
  .btn-amber { background: var(--amber); padding: 14px 32px; font-size: 18px; margin-top: 30px; font-weight: 700; }
  .btn-cyan { background: var(--cyan); padding: 13px 28px; font-size: 18px; }

  /* welcome */
  .welcome { height: 372px; position: relative; padding: 38px 78px 0; }
  .welcome-text { position: relative; z-index: 1; width: 690px; }
  .welcome h2 { font-family: "Marcellus", serif; font-weight: 400; font-size: 42px; line-height: 1.12; color: var(--purple); }
  .welcome h2 span { color: var(--cyan); display: block; }
  .welcome-copy { width: 660px; font-size: 15px; line-height: 1.7; margin: 14px 0 20px; }
  .welcome-photo { position: absolute; right: 78px; top: 24px; width: 344px; height: 343px; background: radial-gradient(ellipse at 50% 45%, #d8b88a 0%, #b88a58 40%, #f5f1ec 75%); }

  /* courses */
  .courses { height: 724px; background: var(--grey-bg); padding-top: 48px; text-align: center; }
  .courses .section-title { color: var(--purple); }
  .section-lead { width: 1030px; margin: 22px auto 0; font-size: 15px; line-height: 1.7; }
  .course-grid { display: flex; gap: 38px; justify-content: center; margin-top: 42px; text-align: left; }
  .course-card { width: 322px; height: 372px; color: var(--white); }
  .course-photo { height: 187px; }
  .course-body { padding: 16px 22px; height: 185px; }
  .course-body h3 { font-family: "Marcellus SC", serif; font-weight: 400; font-size: 23px; margin-bottom: 8px; }
  .course-body p { font-size: 15px; line-height: 1.6; }
  .course-body a { display: inline-block; margin-top: 12px; color: var(--white); font-size: 14px; text-decoration: none; }
  .card-music { background: var(--purple); }
  .card-workshop { background: var(--orange); }
  .card-acting { background: var(--green); }
  .courses .btn-cyan { margin-top: 50px; }

  /* programs */
  .programs { height: 526px; background: var(--purple); color: var(--white); text-align: center; padding-top: 44px; }
  .programs .section-lead { width: 960px; }
  .program-grid { display: flex; justify-content: center; gap: 28px; margin-top: 44px; }
  .program { width: 242px; }
  .program-icon { width: 126px; height: 126px; border-radius: 50%; background: var(--white); margin: 0 auto; display: flex; align-items: center; justify-content: center; }
  .program h3 { font-family: "Marcellus SC", serif; font-weight: 400; font-size: 21px; margin: 22px 0 8px; line-height: 1.2; }
  .program p { font-size: 15px; line-height: 1.6; }
  .program a { color: var(--white); }

  /* testimonial */
  .testimonial { height: 409px; position: relative; background: linear-gradient(100deg, var(--cyan) 0%, var(--cyan-light) 45%, #1a9fcc 100%); color: var(--white); text-align: center; padding-top: 44px; }
  .quote-mark { width: 54px; height: 54px; border-radius: 50%; background: var(--white); margin: 22px auto 0; display: flex; align-items: center; justify-content: center; color: var(--cyan); font-family: "Marcellus", serif; font-size: 46px; line-height: 1; padding-top: 14px; }
  .testimonial blockquote { width: 960px; margin: 22px auto 0; font-size: 16px; line-height: 1.8; }
  .reviewer { display: flex; align-items: center; justify-content: center; gap: 16px; margin-top: 26px; font-family: "Marcellus SC", serif; font-size: 18px; }
  .reviewer-avatar { width: 84px; height: 84px; border-radius: 50%; background: #d9cfc6; border: 3px solid var(--white); }
  .slider-arrow { position: absolute; top: 198px; width: 32px; height: 32px; border-radius: 50%; border: 2px solid var(--white); display: flex; align-items: center; justify-content: center; }
  .slider-prev { left: 80px; }
  .slider-next { right: 80px; }

  /* contact */
  .contact { height: 554px; position: relative; padding-top: 54px; text-align: center; }
  .contact .section-title { color: var(--purple); }
  .contact .section-title span { color: var(--cyan); }
  .contact .section-lead { width: 1030px; }
  .contact-photo { position: absolute; left: 95px; top: 213px; width: 295px; height: 341px; background: linear-gradient(180deg, #f4f4f4 0%, #9ccf6a 35%, #2b2b2b 70%, #f4f4f4 100%); }
  .contact-form { position: absolute; left: 462px; top: 239px; width: 660px; display: grid; grid-template-columns: 1fr 1fr; gap: 11px 15px; text-align: left; }
  .field { height: 43px; background: var(--field); border: 1px solid #dcdcdc; color: #aaa; font-size: 15px; padding: 11px 14px; }
  .field-name { background: var(--white); }
  .field-wide { grid-column: 1 / 3; }
  .field-message { height: 105px; }
  .submit { grid-column: 1 / 3; height: 43px; background: var(--purple); color: var(--white); font-size: 21px; display: flex; align-items: center; justify-content: center; letter-spacing: 1px; }

  /* footer */
  .site-footer { height: 208px; background: var(--purple); position: relative; text-align: center; color: var(--white); }
  .footer-diamond { position: absolute; left: 50%; top: -18px; width: 36px; height: 36px; margin-left: -18px; background: var(--cyan); transform: rotate(45deg); }
  .footer-brand { display: flex; align-items: center; justify-content: center; gap: 12px; padding-top: 56px; }
  .footer-brand .brand-mark { background: var(--cyan); }
  .footer-brand .brand-name { color: var(--white); text-align: left; }
  .copyright { margin-top: 30px; font-size: 15px; letter-spacing: .5px; }
</style>
</head>
<body>

<header class="site-header">
  <div class="brand">
    <span class="brand-mark"></span>
    <span class="brand-name">Bright Kestrel Studio</span>
  </div>
  <div class="call">
    <svg width="46" height="46" viewBox="0 0 24 24" aria-hidden="true"><path fill="#72b84b" d="M6.6 10.8a15.1 15.1 0 0 0 6.6 6.6l2.2-2.2c.3-.3.7-.4 1-.2 1.1.4 2.3.6 3.600.6.6 0 1 .4 1 1V20c0 .6-.4 1-1 1A17 17 0 0 1 3 4c0-.6.4-1 1-1h3.5c.6 0 1 .4 1 1 0 1.3.2 2.5.6 3.6.1.3 0 .7-.2 1z"/></svg>
    <div>
      <div class="call-label">Call Us Now</div>
      <div class="call-number">(404) 555-0142</div>
    </div>
  </div>
</header>

<nav class="main-nav">
  <a class="active" href="#">HOME</a>
  <a href="#">ABOUT US</a>
  <a href="#">COURSES</a>
  <a href="#">PROGRAMS</a>
  <a href="#">OUR TEAM</a>
  <a href="#">TRIAL LESSONS</a>
  <a href="#">GALLERY</a>
  <a href="#">CONTACT US</a>
</nav>

<section class="hero" role="img" aria-label="Photo of students playing guitar and drums in a lesson">
  <div class="hero-inner">
    <h1>BRIGHT KESTREL STUDIO</h1>
    <p>Atlanta's Best Piano, Guitar, Voice, Art Lessons And More, All Taught In Your Home.</p>
    <a class="btn btn-amber" href="#">CONTACT US NOW</a>
  </div>
</section>

<section class="welcome">
  <div class="welcome-text">
    <h2>WELCOME TO <span>BRIGHT KESTREL STUDIO</span></h2>
    <p class="welcome-copy">Atlanta's Best Piano, Guitar, Voice, Art Lessons And More, All Taught In Your Home.<br>It's Time To Play!<br>Learning to play a musical instrument should be an enjoyable journey, not a chore. We exclusively offer in-home, individual music lessons for most instruments including piano, guitar, voice, drums, woodwinds, strings and many more using the...</p>
    <a class="btn btn-cyan" href="#">READ MORE
      <svg width="16" height="14" viewBox="0 0 16 14" aria-hidden="true"><path d="M2 2l5 5-5 5M8 2l5 5-5 5" fill="none" stroke="#fff" stroke-width="2"/></svg></a>
  </div>
  <div class="welcome-photo" role="img" aria-label="Photo of a smiling girl playing an electric guitar"></div>
</section>

<section class="courses">
  <h2 class="section-title">COURSES</h2>
  <p class="section-lead">Bright Kestrel Studio is continually adding new subjects and workshops to its list of courses, responding to the diverse needs and requests of its clients. These are the courses we currently offer instruction in to children, teens and adults, all taught in-home:</p>
  <div class="course-grid">
    <article class="course-card card-music">
      <div class="course-photo" role="img" aria-label="Photo of a drum and guitar lesson" style="background:linear-gradient(135deg,#2e2a28,#7a6e66 50%,#c9c2bb)"></div>
      <div class="course-body">
        <h3>Music Lessons</h3>
        <p>Lorem Ipsum is simply dummy text of the printing and typesetting industry. Lorem Ipsum has been the industry's.</p>
        <a href="#">READ MORE &nbsp;»</a>
      </div>
    </article>
    <article class="course-card card-workshop">
      <div class="course-photo" role="img" aria-label="Photo of children performing at a music workshop" style="background:linear-gradient(135deg,#e8e4dc,#8c7a68 50%,#3a2f28)"></div>
      <div class="course-body">
        <h3>Music Workshops</h3>
        <p>Lorem Ipsum is simply dummy text of the printing and typesetting industry. Lorem Ipsum has been the industry's.</p>
        <a href="#">READ MORE &nbsp;»</a>
      </div>
    </article>
    <article class="course-card card-acting">
      <div class="course-photo" role="img" aria-label="Photo of a costumed stage play cast" style="background:linear-gradient(135deg,#2a1c14,#8a5a3a 50%,#c89a6a)"></div>
      <div class="course-body">
        <h3>Acting Lessons</h3>
        <p>Lorem Ipsum is simply dummy text of the printing and typesetting industry. Lorem Ipsum has been the industry's.</p>
        <a href="#">READ MORE &nbsp;»</a>
      </div>
    </article>
  </div>
  <a class="btn btn-cyan" href="#">VIEW ALL
    <svg width="16" height="14" viewBox="0 0 16 14" aria-hidden="true"><path d="M2 2l5 5-5 5M8 2l5 5-5 5" fill="none" stroke="#fff" stroke-width="2"/></svg></a>
</section>

<section class="programs">
  <h2 class="section-title">OUR PROGRAMS</h2>
  <p class="section-lead">Bright Kestrel Studio offers lessons throughout the entire year via our Weekly and 10-Session Workshop programs. All Bright Kestrel Studio lessons are taught in the comfort and convenience of your own home.</p>
  <div class="program-grid">
    <div class="program">
      <div class="program-icon">
        <svg width="60" height="60" viewBox="0 0 60 60" aria-hidden="true"><path fill="#4b2182" d="M30 4l6 12 10-4-3 12 11 4-10 7 4 9-12-2-5 14-1-14-12 2 4-9-10-7 11-4-3-12 10 4z"/><path d="M30 40v16" stroke="#4b2182" stroke-width="3"/></svg>
      </div>
      <h3>Fall/Spring Program</h3>
      <p>This is our primary program, consisting of 36 weekly lessons offered... <a href="#">READ MORE</a></p>
    </div>
    <div class="program">
      <div class="program-icon">
        <svg width="64" height="64" viewBox="0 0 64 64" aria-hidden="true" fill="#4b2182"><rect x="18" y="6" width="28" height="18" rx="2"/><circle cx="12" cy="34" r="6"/><circle cx="32" cy="34" r="6"/><circle cx="52" cy="34" r="6"/><path d="M2 56c0-8 4-12 10-12s10 4 10 12zM22 56c0-8 4-12 10-12s10 4 10 12zM42 56c0-8 4-12 10-12s10 4 10 12z"/></svg>
      </div>
      <h3>10-Session<br>Workshops</h3>
      <p>All workshops in Theater, Music, Visual... <a href="#">READ MORE</a></p>
    </div>
    <div class="program">
      <div class="program-icon">
        <svg width="62" height="62" viewBox="0 0 62 62" aria-hidden="true"><circle cx="31" cy="31" r="12" fill="#4b2182"/><g stroke="#4b2182" stroke-width="4" stroke-linecap="round"><path d="M31 3v9M31 50v9M3 31h9M50 31h9M11 11l6 6M45 45l6 6M11 51l6-6M45 17l6-6"/></g></svg>
      </div>
      <h3>Summer Session</h3>
      <p>Summer's a great time to try lessons in a new subject or to continue work... <a href="#">READ MORE</a></p>
    </div>
    <div class="program">
      <div class="program-icon">
        <svg width="64" height="64" viewBox="0 0 64 64" aria-hidden="true" fill="#4b2182"><rect x="16" y="8" width="42" height="32" rx="2" fill="none" stroke="#4b2182" stroke-width="4"/><circle cx="10" cy="26" r="6"/><path d="M2 58V42c0-5 3-8 8-8h4l14-8 2 4-14 10v18z"/><path d="M30 30l6-12 6 6 8-10" fill="none" stroke="#4b2182" stroke-width="3"/></svg>
      </div>
      <h3>Trial Lessons</h3>
      <p>The first two lessons taught are considered "trial" lessons, helping you... <a href="#">READ MORE</a></p>
    </div>
  </div>
</section>

<section class="testimonial" role="img" aria-label="Background photo of a microphone over a mixing desk, tinted blue">
  <h2 class="section-title">WHAT OUR CLIENT SAY</h2>
  <div class="quote-mark">&ldquo;</div>
  <blockquote>I can't say enough about how wonderful I think the Bright Kestrel Studio program is. Our teacher makes learning a joy; I never have to ask my kids to practice.</blockquote>
  <div class="reviewer"><span class="reviewer-avatar" role="img" aria-label="Reviewer portrait"></span>- Porchlight Reviews</div>
  <span class="slider-arrow slider-prev"><svg width="12" height="12" viewBox="0 0 12 12" aria-hidden="true"><path d="M8 2L4 6l4 4" fill="none" stroke="#fff" stroke-width="2"/></svg></span>
  <span class="slider-arrow slider-next"><svg width="12" height="12" viewBox="0 0 12 12" aria-hidden="true"><path d="M4 2l4 4-4 4" fill="none" stroke="#fff" stroke-width="2"/></svg></span>
</section>

<section class="contact">
  <h2 class="section-title">CONTACT <span>US</span></h2>
  <p class="section-lead">Want to know more about our programs and courses? Interested in taking a trial lesson? Please call our office at (404) 555-0142 or simply fill out the form below and we will contact you shortly regarding your inquiry. Our instructors teach all over the Greater Atlanta area and it's likely we're already providing lessons in or near your neighborhood.</p>
  <div class="contact-photo" role="img" aria-label="Photo of a young actor in a green costume with arms raised"></div>
  <form class="contact-form">
    <div class="field field-name">Name</div>
    <div class="field">Email</div>
    <div class="field field-wide">Subject</div>
    <div class="field field-wide field-message">Message</div>
    <div class="submit">SUBMIT</div>
  </form>
</section>

<footer class="site-footer">
  <span class="footer-diamond"></span>
  <div class="footer-brand">
    <span class="brand-mark"></span>
    <span class="brand-name">Bright Kestrel Studio</span>
  </div>
  <p class="copyright">© BRIGHT KESTREL STUDIO - 2017. All Rights Reserved.</p>
</footer>

</body>
</html>
```